Brume d'Orvelle Hand Crafted Candles promotional flyer

Hand Crafted Soy Candles - I need a flyer to promote my candles and to give information on care of candles.I want this to use the design and colours I already have for my labels and the photo I have attached.I am aiming at a sophisticated market so would like to reflect this in the design.
Should appeal to sophisticated women who enjoy the pleasure of candles - to enhance their enjoyment of life - gives them the 'brume d'orvelle'.
the candles are hand crafted from all natural ingredients, environmentally friendly and with exquisite fragrances

Target Market(s)

sophisticated females

Industry/Entity Type

Promotional

Font styles to use
Script

Colors
cfeae6
ecdaeb

Requirements
Must have
• something expressing 'brume d'orvelle' - the enjoyment of candles
Should not have
• bright colours

```html
<!DOCTYPE html>
<html lang="en">
<head>
<meta charset="utf-8">
<title>Brume d'Orvelle Hand Crafted Candles – Flyer</title>
<link href="https://fonts.googleapis.com/css2?family=Dancing+Script:wght@400;600&family=Tinos:wght@700&display=swap" rel="stylesheet">
<style>
  :root {
    --lavender: #ecdaeb;
    --mint: #cfeae6;
    --mint-band: #d3ece8;
    --ink: #1f1f22;
    --badge-ring: #f4ecf4;
    --badge-fill: #cfeae6;
    --photo-dark: #3a3d46;
    --photo-glass: #e6e4dc;
    --photo-blue: #2d4f9a;
  }
  * { margin: 0; padding: 0; box-sizing: border-box; }
  html, body { width: 1200px; height: 849px; overflow: hidden; background: #fff; }
  .flyer { position: relative; width: 1200px; height: 849px; overflow: hidden; color: var(--ink);
    font-family: "Dancing Script", cursive; }

  .panel-top { position: absolute; left: 0; top: 0; width: 1200px; height: 463px; background: var(--lavender); }
  .panel-bottom { position: absolute; left: 0; top: 463px; width: 1200px; height: 386px; background: var(--mint); }

  .badge { position: absolute; left: 120px; top: 57px; width: 340px; height: 340px; }
  .badge-name { position: absolute; left: 120px; top: 188px; width: 340px; text-align: center;
    font-size: 34px; font-weight: 400; line-height: 50px; color: var(--ink); }

  .bullets { list-style: none; }
  .bullets li { position: relative; padding-left: 20px; }
  .bullets li::before { content: ""; position: absolute; left: 3px; top: 8px; width: 6px; height: 6px;
    border-radius: 50%; background: var(--ink); }

  .info { position: absolute; left: 612px; top: 38px; width: 548px; font-size: 12.6px; line-height: 21.6px; }
  .info .bullets li { white-space: nowrap; }
  .info .bullets li.two-line { line-height: 16px; padding-top: 3px; padding-bottom: 3px; }
  .info .bullets li.two-line::before { top: 8px; }
  .section-band { background: var(--mint-band); font-size: 15px; font-weight: 600; line-height: 22px;
    padding-left: 6px; margin: 2px 0 2px -6px; }

  .contact { position: absolute; left: 616px; top: 407px; font-family: "Tinos", serif; font-weight: 700;
    font-size: 16.5px; line-height: 25px; white-space: nowrap; }
  .contact .gap { display: inline-block; width: 22px; }

  .care { position: absolute; left: 56px; top: 490px; width: 580px; }
  .care h2 { font-size: 20px; font-weight: 400; line-height: 27px; margin-bottom: 2px; white-space: nowrap; }
  .care .bullets { font-size: 12px; }
  .care .bullets li { line-height: 16px; margin-bottom: 5px; padding-left: 18px; white-space: nowrap; }
  .care .bullets li::before { left: 2px; top: 6px; width: 5px; height: 5px; }

  .product-photo { position: absolute; left: 648px; top: 600px; width: 494px; height: 213px; border-radius: 4px;
    background: linear-gradient(90deg, var(--photo-dark) 0%, #c9ccc8 28%, var(--photo-glass) 55%, #d8d6cc 78%, var(--photo-blue) 100%); }
</style>
</head>
<body>
<div class="flyer">
  <section class="panel-top"></section>
  <section class="panel-bottom"></section>

  <svg class="badge" viewBox="0 0 340 340" aria-hidden="true">
    <circle cx="170" cy="170" r="166" fill="var(--badge-fill)" stroke="var(--badge-ring)" stroke-width="7"/>
  </svg>
  <div class="badge-name">Brume d'Orvelle<br>Hand Crafted Candles</div>

  <div class="info">
    <ul class="bullets">
      <li>Brume d'Orvelle - an exuberant enjoyment of life - these candles will fill you with "Brume d'Orvelle".</li>
      <li>Candles are lovingly hand - poured and use only the finest of ingredients and fragrances</li>
      <li>Hand crafted soy candle creations</li>
      <li>Completely non - toxic</li>
      <li>Exquisite fragrances</li>
      <li>Clean burning</li>
      <li>Environmentally friendly.</li>
    </ul>
    <div class="section-band">Why soy wax?</div>
    <ul class="bullets">
      <li>Soft smooth wax that burns clean - no soot or smoke</li>
      <li>Soy wax candles burn up to 50% longer than traditional paraffin candles</li>
      <li class="two-line">Made form soya beans, a renewable natural resource that supports and sustains agriculture -<br>it is biodegradable and environmentally friendly.</li>
      <li>Soy wax burns cooler than paraffin and disperse the fragrance more fully.</li>
    </ul>
    <div class="section-band">Containers can be refilled</div>
    <ul class="bullets">
      <li>I offer a refill service - if you return you containers to me I can refill with the fragrance of your choice.</li>
      <li>Or if you have a special container you would like to use for your candle just contact me for a quote.</li>
      <li>I have a wide range of fragrances - please contact me for details.</li>
    </ul>
  </div>

  <div class="contact">
    <div>Mobile: 021 555 0148</div>
    <div>Email: hello@brumedorvelle.example<span class="gap"></span>Website: www.brumedorvelle.example</div>
  </div>

  <div class="care">
    <h2>How to care for your candle - the following tips will ensure you have a long<br>lasting, fully fragranced candle</h2>
    <ul class="bullets">
      <li>When lighting you candle for the first time, allow the wax to melt all the way to the sides of the container -<br>this creates a 'memory' and avoids 'tunnelling' as the candle burns.</li>
      <li>Always trim the wick to about 6 - 8mm before re-lighting your candle. This will ensure a long lasting candle,<br>minimise soot and remove any mushrooming of the wick from a previous burn.</li>
      <li>It is preferable to use a candle 'snuffer' to extinguish the flame, or a lid if the candle has one. Alternatively,<br>you can dip the wick into the melted wax and then straightening. This wil stop the wick from smoking and help<br>with relighting.</li>
      <li>All Brume d'Orvelle candles are hand poured not mass produced - although every effort is made to ensure<br>consistency, every candle may be different.</li>
      <li>Sometimes you may notice darker patches or wet spots - this is not a fault it is just the natural way the wax has<br>set - it does not affect the candle in anyway.</li>
      <li>The top of the candle may also appear slightly uneven - this is just a sign of natural soy wax being hand poured.</li>
      <li>Do not leave your candle in the sunlight as it may turn a yellow colour - again this does not affect the candle in<br>anyway - it just loses its creamy white colour.</li>
      <li>As these candles contain no preservatives or chemicals it is recommended that they should be used within 6 months.</li>
    </ul>
  </div>

  <div class="product-photo" role="img" aria-label="Photograph of four soy candles in a row: a black glass jar, two clear jars with silver lids and a small blue votive, each with a round label"></div>
</div>
</body>
</html>
```